We need a company profile design 8 + cover

The company profile is attached below, we need to renew the whole thing with full modification. content and page arrangement is the same. All should be A5 size printable and electronic copies.

I attached logo and colors for identity, please use logo colors as main scheme colours

We need 2 copies Arabic and English

Font styles to use
Sans Serif

Requirements
Nice to have
• Please let us know how we can use the designs to edit in Arabic

```html
<!DOCTYPE html>
<html lang="en">
<head>
<meta charset="utf-8">
<title>Nova Scholar – Company Profile</title>
<link href="https://fonts.googleapis.com/css2?family=Montserrat:wght@300;600;800&family=Lato:ital,wght@0,300;0,400;0,700;1,300;1,400&display=swap" rel="stylesheet">
<style>
:root{
  --navy:#1f3167;
  --blue:#34509e;
  --lime:#b8e62a;
  --green:#9bc53d;
  --stage:#6b6b6b;
  --paper:#ffffff;
  --ink:#1e2230;
}
*{box-sizing:border-box;margin:0;padding:0}
html,body{width:1200px;height:1200px;overflow:hidden}
body{background:var(--stage);font-family:'Lato',sans-serif;color:var(--ink);position:relative}
.spread{position:absolute;background:var(--paper);box-shadow:0 3px 10px rgba(0,0,0,.35);overflow:hidden}
.spread-cover{left:113px;top:49px;width:741px;height:524px}
.spread-inner{left:346px;top:599px;width:742px;height:525px}
.abs{position:absolute}
.page-fold{position:absolute;top:0;bottom:0;width:60px;background:linear-gradient(90deg,rgba(0,0,0,.1),rgba(0,0,0,0))}
.rule{position:absolute;height:3px;background:var(--lime)}
.brand{font-family:'Lato',sans-serif;font-weight:700;color:var(--navy);text-align:center;line-height:1.05;letter-spacing:1px}
.brand-box{left:52px;top:18px;width:159px;height:139px;background:#fff;border:2px solid var(--blue);display:flex;flex-direction:column;align-items:center;justify-content:center;z-index:3}
.brand-box .brand{font-size:26px}
.brand-mark{width:14px;height:14px;background:var(--navy);margin-bottom:8px}
.lime-frame{border:3px solid var(--lime)}
.photo{position:absolute}
.photo-city{left:17px;top:123px;width:354px;height:330px;background:linear-gradient(160deg,#4a66ad,#2f4a94 60%,#3a58a4)}
.cover-frame{left:93px;top:46px;width:246px;height:288px;z-index:2}
.slogan{left:124px;top:275px;font-family:'Montserrat',sans-serif;font-weight:800;font-size:27px;line-height:1.1;color:#fff;z-index:4}
.slogan span{display:block;color:var(--lime)}
.contact{left:22px;top:434px;width:207px;height:90px;background:var(--green);color:#fff;font-size:8.5px;line-height:1.2;padding:6px 8px 0 18px}
.contact p{position:relative;margin-bottom:8px}
.contact svg{position:absolute;left:-12px;top:1px}
.links{left:238px;top:457px;font-size:7.6px;line-height:1;color:var(--ink)}
.links li{list-style:none;margin-bottom:6.5px;display:flex;align-items:center;gap:4px}
.links li::before{content:"";width:5px;height:5px;border-radius:50%;background:var(--navy)}
.cover-right{left:371px;top:0;width:370px;height:524px;background:linear-gradient(90deg,#e3e3e3,#fff 20%)}
.brand-top{left:481px;top:42px;width:150px;font-size:20px}
.students-frame{left:446px;top:112px;width:278px;height:250px}
.photo-students{left:382px;top:123px;width:323px;height:330px;background:linear-gradient(170deg,#8a7c6a,#3e3a36 55%,#2a2a2e)}
.title-box{left:454px;top:399px;width:242px;height:90px;background:var(--navy);padding:6px 12px;font-family:'Montserrat',sans-serif;font-weight:800;font-size:22px;line-height:1.13;color:#fff}
.title-box span{color:var(--lime)}
.web{left:505px;top:533px;font-size:13px;display:flex;align-items:center;gap:6px}
.quote{position:absolute;left:41px;width:165px;background:var(--green);color:#fff;font-style:italic;font-weight:300;font-size:12.5px;line-height:1.15;padding:5px 9px;z-index:3}
.q{font-family:'Montserrat',sans-serif;font-style:normal;font-weight:800;font-size:12px}
.photo-leader{left:16px;top:47px;width:355px;height:186px;background:linear-gradient(120deg,#8a9a9c,#dcdcd6 55%,#b9b3a8)}
.photo-elder{left:16px;top:274px;width:355px;height:186px;background:linear-gradient(120deg,#5d7b5a,#7f8f6e 50%,#4e4438)}
.caption{position:absolute;left:16px;width:355px;background:rgba(31,49,103,.82);color:#fff;font-size:10px;font-weight:700;text-align:center;display:flex;align-items:center;justify-content:center}
.folio{position:absolute;top:496px;display:flex;align-items:center;gap:6px;font-size:9px;letter-spacing:1.5px}
.folio b{background:var(--green);color:#fff;font-size:8px;width:22px;height:14px;border-radius:2px;display:flex;align-items:center;justify-content:center;letter-spacing:0}
.who{left:388px;top:38px;width:337px;height:178px;border:2px solid var(--navy)}
.who-title{left:417px;top:16px;width:212px;height:50px;background:var(--green);color:#fff;font-family:'Montserrat',sans-serif;font-weight:300;font-size:27px;display:flex;align-items:center;justify-content:center;gap:8px}
.who-title b{font-weight:800}
.body-text{font-size:8.3px;line-height:1.28;text-align:justify}
.who-text{left:398px;top:77px;width:318px}
.who-text p{margin-bottom:4px}
.who-text strong{color:var(--navy);font-weight:700;font-size:9.5px}
.box{position:absolute;left:388px;width:337px;border:2px solid}
.vision{top:237px;height:62px;border-color:var(--lime);padding:3px 8px}
.mission{top:311px;height:76px;border-color:var(--navy);padding:3px 8px}
.box h3{font-family:'Montserrat',sans-serif;font-weight:800;font-size:17px;color:var(--navy);display:flex;align-items:center;gap:4px;margin-bottom:2px}
.box h3::after{content:"";flex:1;height:1px;background:#888}
.mission h3{flex-direction:row-reverse}
.values{left:386px;top:399px;width:338px;height:87px;background:var(--navy);color:#fff}
.values-head{position:absolute;left:10px;top:17px;font-family:'Montserrat',sans-serif;font-weight:300;font-size:19px;line-height:1.15}
.values-head b{display:block;font-weight:800}
.values-list{position:absolute;left:118px;top:6px;width:210px;font-size:8.6px;font-weight:700;line-height:1.1}
.values-list li{list-style:none;padding-left:14px;position:relative;margin-bottom:4px}
.values-list svg{position:absolute;left:0;top:0}
</style>
</head>
<body>

<section class="spread spread-cover" aria-label="Cover spread">
  <div class="rule" style="left:0;top:18px;width:46px"></div>
  <div role="img" aria-label="Aerial view of a city stadium in blue tones" class="photo photo-city"></div>
  <div class="abs lime-frame cover-frame"></div>
  <div class="abs brand-box"><span class="brand-mark"></span><span class="brand">NOVA<br>SCHOLAR</span></div>
  <h1 class="abs slogan">BE AMONG<span>THE BEST</span></h1>

  <div class="abs contact">
    <p><svg width="7" height="9" viewBox="0 0 7 9"><path d="M3.5 0a3.2 3.2 0 0 0-3.2 3.2C.3 5.6 3.5 9 3.5 9s3.2-3.4 3.2-5.8A3.2 3.2 0 0 0 3.5 0zm0 4.4a1.2 1.2 0 1 1 0-2.4 1.2 1.2 0 0 1 0 2.4z" fill="#fff"/></svg>Harbor View Tower / Marina Club<br>Suite 31, 3rd Floor, PO Box – 4820</p>
    <p><svg width="8" height="8" viewBox="0 0 8 8"><path d="M1.6 0l1.5 1.8-.8 1a5 5 0 0 0 2.7 2.7l1-.8L8 6.2 6.9 8C3.1 7.6.4 4.9 0 1.1z" fill="#fff"/></svg>+971 2 555 01 23 | +971 50 555 0147<br>+971 52 555 0188 | +971 50 5550199</p>
    <p><svg width="8" height="6" viewBox="0 0 8 6"><rect width="8" height="6" fill="#fff"/><path d="M0 0l4 3.4L8 0" stroke="#9bc53d" fill="none"/></svg>hello@novascholar.ae</p>
  </div>
  <ul class="abs links">
    <li>www.novascholar.ae</li>
    <li>social/novascholar</li>
    <li>updates/novascholar_ae</li>
    <li>novascholar.uae</li>
  </ul>

  <div class="abs cover-right"></div>
  <div class="abs brand brand-top">NOVA<br>SCHOLAR</div>
  <div class="abs lime-frame students-frame"></div>
  <div role="img" aria-label="Group of smiling international students seated on stairs" class="photo photo-students"></div>
  <h2 class="abs title-box">ACADEMIC AND<br>STUDY ABROAD<br><span>SERVICES</span></h2>
  <div class="abs web"><svg width="12" height="12" viewBox="0 0 12 12" fill="none" stroke="#1e2230" stroke-width="1"><circle cx="6" cy="6" r="5.3"/><ellipse cx="6" cy="6" rx="2.3" ry="5.3"/><path d="M.7 6h10.6M1.6 3.3h8.8M1.6 8.7h8.8"/></svg>www.novascholar.ae</div>
  <div class="rule" style="left:456px;top:521px;width:235px"></div>
</section>

<section class="spread spread-inner" aria-label="Inner spread pages 1 and 2">
  <div class="page-fold" style="left:372px"></div>
  <div class="rule" style="left:0;top:17px;width:36px"></div>
  <div role="img" aria-label="Portrait of a national leader in traditional white headdress" class="photo photo-leader"></div>
  <blockquote class="quote" style="top:17px;height:62px"><span class="q">“</span> There is no place in the future for those who lack science and knowledge <span class="q">”</span></blockquote>
  <div class="caption" style="top:209px;height:24px">- H.E. Rashid Al Noor</div>

  <div class="rule" style="left:0;top:246px;width:36px"></div>
  <div role="img" aria-label="Portrait of a smiling elder statesman waving" class="photo photo-elder"></div>
  <blockquote class="quote" style="top:249px;height:72px"><span class="q">“</span> Education is the most powerful weapon which you can use to change the world <span class="q">”</span></blockquote>
  <div class="caption" style="top:435px;height:26px">- Amara Okafor</div>
  <div class="folio" style="left:16px"><b>01</b>www.novascholar.ae</div>

  <div class="rule" style="left:371px;top:17px;width:40px"></div>
  <div class="abs who"></div>
  <h2 class="abs who-title"><b>WHO</b> WE ARE</h2>
  <div class="abs body-text who-text">
    <p><strong>NOVA SCHOLAR</strong> is the fastest growing educational consultancy and study abroad services in UAE. It is officially recognized by the Higher Education Authority, Global Study Council, EduAgents Network and QualityCert 9001.</p>
    <p>Established in 2015, NOVA SCHOLAR provides professional consultancy services to help aspiring students find a suitable overseas educational institution in USA, UK, Australia, Malaysia, Europe, Middle East, South Africa and more.</p>
    <p>We take pride in our holistic program that helps every student make the right career choice, find the right course, what the student need and the government vision.</p>
    <p>We act as study abroad consultants for various government sectors and corporations.</p>
  </div>

  <div class="box vision">
    <h3>VISION</h3>
    <p class="body-text">To be leading the educational consultancy in the region by providing customized and up to date educational services to students and educational institutions abroad</p>
  </div>
  <div class="box mission">
    <h3>MISSION</h3>
    <p class="body-text">To provide students from all the countries with the needed and qualified services for abroad studies through an integrated system of facilities, consultancy services and guidance through building strategic partnerships with the best universities from all over the world.</p>
  </div>

  <div class="abs values">
    <div class="values-head">OUR<b>VALUES</b></div>
    <svg class="abs" style="left:90px;top:8px" width="14" height="70" viewBox="0 0 14 70"><path d="M2 0v28l10 7-10 7v28" stroke="#fff" stroke-width="2.4" fill="none"/></svg>
    <ul class="values-list">
      <li><svg width="9" height="8" viewBox="0 0 9 8"><path d="M1 4l2.5 2.5L8 1" stroke="#9bc53d" stroke-width="1.8" fill="none"/></svg>Credibility</li>
      <li><svg width="9" height="8" viewBox="0 0 9 8"><path d="M1 4l2.5 2.5L8 1" stroke="#9bc53d" stroke-width="1.8" fill="none"/></svg>Social Responsibility</li>
      <li><svg width="9" height="8" viewBox="0 0 9 8"><path d="M1 4l2.5 2.5L8 1" stroke="#9bc53d" stroke-width="1.8" fill="none"/></svg>Excellence in Services delivery</li>
      <li><svg width="9" height="8" viewBox="0 0 9 8"><path d="M1 4l2.5 2.5L8 1" stroke="#9bc53d" stroke-width="1.8" fill="none"/></svg>Strengthening Partnerships</li>
      <li><svg width="9" height="8" viewBox="0 0 9 8"><path d="M1 4l2.5 2.5L8 1" stroke="#9bc53d" stroke-width="1.8" fill="none"/></svg>Implementing best practises in the educational consultancy</li>
    </ul>
  </div>
  <div class="folio" style="left:386px"><b>02</b>www.novascholar.ae</div>
</section>

</body>
</html>
```